Exciting new vermouth brand needs a brilliant label!

We need a label design for an exciting new premium Italian Vermouth brand called Lunavera Vermouth.

Lunavera Vermouth is based on a recipe that has been handed down for four generations and is made in the traditional way in the Piedmonte region of Northern Italy.

Lunavera, which means 'heavenly' in Italian has been designed to elevate classic cocktails such as the Negroni, Americano and Manhattan with a base of Italian wine blended with botanicals such as wormwood, orange peel, rhubarb and cinchona. It has a delicately balanced bittersweet profile with hints of vanilla and citrus.

Its competitors include brands such as Vecchia Ricetta, Brunetti and Fabrizzi (see the uploaded brief for more examples).

The label is for a 50cl dark bottle (please refer to the uploaded brief) and should be based on maximum dimensions of 70mm (width) x 110mm (height). There is no limit to embellishments such as foil printing, embossing or any other premium finishes. The label does not necessarily need to be rectangular.

Feedback will be given quickly and constructively after submissions to ensure that the process is as fair and useful as possible for everyone.

Target Market(s)

25-45 year old Europeans, 50:50 female:male

Industry/Entity Type

Wine / Spirits / Vermouth

Requirements
Must have
• Fantastic design that is distinct from competitors, a premium feel and great lettering.
Should not have
• Generic images or patterns that do not relate to the brand (Lunavera) or the product

```html
<!DOCTYPE html>
<html lang="en">
<head>
<meta charset="utf-8">
<title>Lunavera Vermouth – Label</title>
<link rel="stylesheet" href="https://fonts.googleapis.com/css2?family=Cinzel:wght@400;600&family=Great+Vibes&display=swap">
<style>
  :root {
    --bg: #14181d;
    --label: #0d0e10;
    --label-edge: #1c1e22;
    --copper: #d8893a;
    --copper-light: #f0a955;
    --silver: #d9dcdf;
    --silver-dark: #8e9297;
    --band: #17191c;
  }
  * { margin: 0; padding: 0; box-sizing: border-box; }
  html, body { width: 1200px; height: 800px; overflow: hidden; }
  body {
    background: var(--bg);
    display: flex;
    align-items: center;
    justify-content: center;
    font-family: "Cinzel", "Times New Roman", serif;
  }
  .label {
    position: relative;
    width: 440px;
    height: 692px;
    background: var(--label);
    border: 1px solid var(--label-edge);
    box-shadow: 0 20px 60px rgba(0,0,0,.5);
    text-align: center;
  }
  .label__vintage {
    position: absolute; top: 70px; left: 0; right: 0;
    color: var(--copper); font-size: 15px; letter-spacing: 1px;
  }
  .label__brand {
    position: absolute; top: 100px; left: 0; right: 0;
    color: var(--copper-light); font-size: 44px; font-weight: 600; letter-spacing: 7px;
  }
  .label__product {
    position: absolute; top: 150px; left: 0; right: 0;
    font-family: "Great Vibes", cursive;
    color: var(--silver); font-size: 46px;
  }
  .label__band {
    position: absolute; left: 0; right: 0; top: 320px; height: 76px;
    background: var(--band);
    border-top: 1px solid #2a2d31;
    border-bottom: 1px solid #2a2d31;
  }
  .label__band::before, .label__band::after {
    content: ""; position: absolute; left: 0; right: 0; height: 1px; background: #33363a;
  }
  .label__band::before { top: 8px; }
  .label__band::after { bottom: 8px; }
  .label__seal {
    position: absolute; left: 50%; top: 270px; width: 176px; height: 176px;
    margin-left: -88px;
  }
  .label__seal-text {
    position: absolute; left: 0; right: 0; top: 62px;
    color: var(--silver); font-size: 19px; letter-spacing: 3px;
  }
  .label__seal-year {
    position: absolute; left: 0; right: 0; top: 92px;
    color: var(--silver); font-size: 12px; letter-spacing: 3px;
  }
  .label__grade {
    position: absolute; top: 485px; left: 0; right: 0;
    color: var(--silver); font-size: 22px; letter-spacing: 3px;
  }
  .label__tagline {
    position: absolute; top: 520px; left: 0; right: 0;
    color: var(--copper); font-size: 18px; letter-spacing: 1px;
  }
  .label__volume-band {
    position: absolute; left: 0; right: 0; top: 595px; height: 36px;
    background: linear-gradient(180deg, #e9ebed, var(--silver-dark) 55%, #c9ccd0);
    color: #2b2d31; font-size: 12px; letter-spacing: 3px; line-height: 36px;
  }
  .label__copper-rule {
    position: absolute; left: 0; right: 0; top: 638px; height: 3px; background: var(--copper);
  }
</style>
</head>
<body>
  <main class="label">
    <div class="label__vintage">2023</div>
    <h1 class="label__brand">LUNAVERA</h1>
    <div class="label__product">Vermouth</div>

    <div class="label__band"></div>
    <div class="label__seal">
      <svg width="176" height="176" viewBox="0 0 176 176">
        <circle cx="88" cy="88" r="86" fill="#111214" stroke="#5e6166" stroke-width="1.5"/>
        <circle cx="88" cy="88" r="80" fill="none" stroke="var(--copper)" stroke-width="2.5"/>
      </svg>
      <div class="label__seal-text">LUNAVERA</div>
      <div class="label__seal-year">EST 2023</div>
    </div>

    <div class="label__grade">PREMIUM</div>
    <div class="label__tagline">Elevate your cocktails</div>

    <div class="label__volume-band">50CL</div>
    <div class="label__copper-rule"></div>
  </main>
</body>
</html>
```